New eyelid plastic surgery office needs a business card design-Eyelid Surgery Partners of Brennor

I recently used SketchHarbor for my logo design and was very pleased with creativity and results. It was a difficult decision for me. Now I would like to create a business card based on this logo, which I will attach.

The text should be easily legible as some of my patients have difficulty seeing, but I would like a subtle, sophisticated artistry also evident to make the card memorable. Would like the card based on a similar color scheme as the logo but the inverse or other complementary colors may prove interesting

A good question was asked...my concern about my visually impaired patients was really my desire to avoid italicized or calligraphic type fonts that may be hard to read. Standard font size for a business card would be fine. Thanks!

Thank you so much for the great work so far. I wanted to give you my particular contact information to see if that would change the look of the cards. Martin Pellowby, MD Address: 2817 Larkmoor Avenue, Suite 205 Wilmington, NC 28517 Phone: 910-555-0183 Fax: 910-555-0184 Website: www.brennorlidclinic.example Please delete the email slot from the card. Thanks so much!

Reason: Last minute consideration. So many great revisions right now!

Plastic

```html
<!DOCTYPE html>
<html lang="en">
<head>
<meta charset="utf-8">
<title>Eyelid Surgery Partners of Brennor – Business Card</title>
<link rel="stylesheet" href="https://fonts.googleapis.com/css2?family=PT+Sans:wght@400;700&display=swap">
<style>
  :root {
    --page-bg: #e9e9e9;
    --card-black: #050505;
    --card-grey-light: #cfcfcf;
    --card-grey-dark: #8c8c8c;
    --band-grey: #a9a9a9;
    --brand-blue: #2b5bab;
    --ink: #111111;
  }
  * { margin: 0; padding: 0; box-sizing: border-box; }
  html, body {
    width: 1200px;
    height: 888px;
    overflow: hidden;
    background: var(--page-bg);
  }
  .card {
    position: absolute;
    left: 60px;
    top: 134px;
    width: 1080px;
    height: 620px;
    overflow: hidden;
    box-shadow: 0 6px 18px rgba(0, 0, 0, 0.25);
    font-family: "PT Sans", sans-serif;
    color: var(--ink);
  }
  .card-backdrop {
    position: absolute;
    inset: 0;
    width: 100%;
    height: 100%;
  }
  .brand-name {
    position: absolute;
    top: 92px;
    left: 0;
    width: 100%;
    text-align: center;
    font-weight: 700;
    font-size: 58px;
    line-height: 1.05;
    letter-spacing: 1px;
    text-transform: uppercase;
    color: var(--brand-blue);
  }
  .contact-block {
    position: absolute;
    left: 60px;
    top: 392px;
    padding-left: 22px;
    border-left: 2px solid var(--ink);
    font-weight: 700;
  }
  .contact-label {
    font-size: 24px;
    line-height: 34px;
  }
  .contact-name {
    margin: 6px 0 10px 170px;
    font-size: 40px;
    line-height: 46px;
  }
  .contact-row {
    display: flex;
    font-size: 25px;
    line-height: 31px;
  }
  .contact-row dt { width: 120px; }
  .contact-row dd::before { content: ": "; }
</style>
</head>
<body>
  <section class="card">
    <svg class="card-backdrop" viewBox="0 0 1080 620" preserveAspectRatio="none" aria-hidden="true">
      <defs>
        <linearGradient id="lower-grey" x1="0" y1="0" x2="0.3" y2="1">
          <stop offset="0" stop-color="var(--card-grey-light)"/>
          <stop offset="1" stop-color="var(--card-grey-dark)"/>
        </linearGradient>
      </defs>
      <rect width="1080" height="620" fill="url(#lower-grey)"/>
      <path d="M0 0 H1080 V290 C880 430 480 440 0 250 Z" fill="var(--band-grey)"/>
      <path d="M0 0 H1080 V262 C880 400 480 410 0 226 Z" fill="var(--card-black)"/>
    </svg>

    <h1 class="brand-name">Eyelid Surgery Partners<br>of Brennor</h1>

    <div class="contact-block">
      <p class="contact-label">Contact&nbsp;&nbsp;:</p>
      <p class="contact-name">Martin Pellowby, MD</p>
      <dl>
        <div class="contact-row"><dt>Address</dt><dd>2817 Larkmoor Avenue, Suite 205 Wilmington, NC 28517</dd></div>
        <div class="contact-row"><dt>Phone</dt><dd>910 - 555 - 0183</dd></div>
        <div class="contact-row"><dt>Fax</dt><dd>910 - 555 - 0184</dd></div>
        <div class="contact-row"><dt>web</dt><dd>www.brennorlidclinic.example</dd></div>
      </dl>
    </div>
  </section>
</body>
</html>
```